Recruitment Site Design

We need a design for the login page, about page, and inner pages of a recruitment site for an oil and gas company. Design should be modern, sleek, professional and colors can be blue, green, white, orange or any other recommended colors.

Please also take into consideration that once the users login, they will need to access a form to fill in their information.

** UPDATE: Kindly provide a design for the inner information page consistent with the outer design. Attached is a picture of the basic structure. ***
Updates

Please provide a design for inner pages as shown in the design brief consistent with the registration page provided. 

Reason: We're extending it to get more inside pages.

Target Market(s)

Professionals looking for a career in the oil and gas industry in the Middle East.

Industry/Entity Type

Oil And Gas

Requirements
Must have
• Sleek design

```html
<!DOCTYPE html>
<html lang="en">
<head>
<meta charset="utf-8">
<title>Meridian Crude — Careers</title>
<link rel="stylesheet" href="https://fonts.googleapis.com/css2?family=Lato:ital,wght@0,300;0,400;0,700;1,400&display=swap">
<style>
:root{
  --brand-blue:#1f6fb8;
  --band-top:#3b93d3;
  --band-bottom:#1b5fa6;
  --heading-blue:#2a7cc4;
  --text-grey:#6b6b6b;
  --text-dark:#4a4a4a;
  --hero-grey:#ebebeb;
  --white:#ffffff;
  --footer-dark:#161616;
  --orange-top:#ffc21e;
  --orange-bottom:#f08a0a;
  --button-top:#e4e4e4;
  --button-bottom:#8d8d8d;
}
*{box-sizing:border-box;margin:0;padding:0}
html,body{width:1200px;height:1100px;overflow:hidden}
body{position:relative;background:var(--white);font-family:"Lato",Arial,sans-serif;color:var(--text-grey)}

.site-header{position:absolute;left:0;top:0;width:1200px;height:100px;background:var(--white)}
.brand{position:absolute;left:248px;top:38px;font-weight:400;font-size:26px;color:var(--brand-blue)}
.main-nav{position:absolute;left:596px;top:34px;height:40px;display:flex}
.main-nav a{display:block;padding:0 20px;line-height:40px;font-size:12.5px;font-weight:700;color:#6a6a6a;text-decoration:none;border-left:1px solid #e2e2e2}
.main-nav a:first-child{border-left:none}

.promo-band{position:absolute;left:0;top:100px;width:1200px;height:96px;background:linear-gradient(var(--band-top),var(--band-bottom));box-shadow:0 -2px 4px rgba(0,0,0,.15)}
.promo-band h2{position:absolute;left:247px;top:32px;font-weight:400;font-size:24px;color:var(--white)}
.btn-register{position:absolute;left:758px;top:28px;width:163px;height:42px;border-radius:3px;background:linear-gradient(var(--orange-top),var(--orange-bottom));color:var(--white);font-weight:700;font-size:20px;text-align:center;line-height:42px;box-shadow:0 2px 3px rgba(0,0,0,.3);text-shadow:0 1px 1px rgba(0,0,0,.25)}

.hero{position:absolute;left:0;top:196px;width:1200px;height:330px;background:radial-gradient(ellipse at 50% 40%,#f6f6f6 0%,var(--hero-grey) 70%,#f4f4f4 100%)}
.hero-photo{position:absolute;left:232px;top:12px;width:318px;height:281px;background:radial-gradient(ellipse at 45% 50%,#c58a5a 0%,#8e96a0 40%,#c9d0d8 65%,rgba(235,235,235,0) 100%)}
.hero h1{position:absolute;left:548px;top:58px;font-weight:300;font-size:54px;color:#5f5f5f}
.hero p{position:absolute;left:554px;top:128px;width:400px;font-weight:300;font-size:15px;line-height:18px;color:var(--text-grey)}
.hero p strong{font-weight:700;color:var(--text-dark)}
.btn-grey{display:block;background:linear-gradient(var(--button-top),var(--button-bottom));color:var(--white);font-weight:700;text-align:center;border-radius:2px;box-shadow:0 1px 2px rgba(0,0,0,.35);text-shadow:0 1px 1px rgba(0,0,0,.35)}
.btn-learn{position:absolute;left:554px;top:238px;width:110px;height:27px;line-height:27px;font-size:14px}

.content-panel{position:absolute;z-index:2;left:241px;top:526px;width:720px;height:425px;background:var(--white);box-shadow:0 4px 6px rgba(0,0,0,.2)}
.feature{position:absolute;width:210px}
.feature h3{font-weight:400;font-size:24px;color:var(--heading-blue);white-space:nowrap}
.feature p{margin:14px 0 0 6px;width:196px;font-weight:300;font-size:9.8px;line-height:12.3px;color:var(--text-grey)}
.feature .btn-more{margin:14px 0 0 4px;width:46px;height:17px;line-height:17px;font-size:10px}

.site-footer{position:absolute;left:0;top:919px;width:1200px;height:181px;background:var(--footer-dark)}
.footer-nav{position:absolute;left:279px;top:105px;font-size:12px;font-style:italic;color:#e0e0e0}
.footer-brand{position:absolute;right:270px;top:85px;font-weight:400;font-size:25px;color:var(--brand-blue)}
.footer-legal{position:absolute;right:274px;top:121px;font-size:7.5px;font-style:italic;color:#d0d0d0}
</style>
</head>
<body>
<header class="site-header">
  <div class="brand">Meridian Crude</div>
  <nav class="main-nav">
    <a href="#">Register</a><a href="#">Available Jobs</a><a href="#">FAQs</a><a href="#">Contact</a>
  </nav>
</header>

<section class="promo-band">
  <h2>Lorem Ipsum Consectetur Adipiscing Elit</h2>
  <a class="btn-register">Register now</a>
</section>

<section class="hero">
  <div class="hero-photo" role="img" aria-label="Oil field worker in hard hat and safety vest standing in front of a pump jack"></div>
  <h1>Lorem Ipsum Elit</h1>
  <p><strong>Duis aute irure dolor in reprehenderit in voluptate.</strong> Lorem ipsum dolor sit amet, consectetur adipiscing elit, sed do eiusmod tempor incididunt ut labore et dolore magna aliqua. Ut enim ad minim veniam, quis nostrud exercitation ullamco laboris nisi ut aliquip ex ea commodo consequat.</p>
  <a class="btn-grey btn-learn">Learn More</a>
</section>

<main class="content-panel">
  <article class="feature" style="left:22px;top:48px"><h3>Lorem Ipsum Elit</h3><p>Lorem ipsum dolor sit amet, consectetur adipiscing elit. Curabitur lorem justo, euismod quis feugiat eu, malesuada eget erat. Class aptent taciti sociosqu ad litora torquent per conubia nostra, per inceptos himenaeos.</p><a class="btn-grey btn-more">More</a></article>
  <article class="feature" style="left:263px;top:48px"><h3>Consectetur Elit</h3><p>Lorem ipsum dolor sit amet, consectetur adipiscing elit. Curabitur lorem justo, euismod quis feugiat eu, malesuada eget erat. Class aptent taciti sociosqu ad litora torquent per conubia nostra, per inceptos himenaeos.</p><a class="btn-grey btn-more">More</a></article>
  <article class="feature" style="left:499px;top:48px"><h3>Adipiscing Lorem</h3><p>Lorem ipsum dolor sit amet, consectetur adipiscing elit. Curabitur lorem justo, euismod quis feugiat eu, malesuada eget erat. Class aptent taciti sociosqu ad litora torquent per conubia nostra, per inceptos himenaeos.</p><a class="btn-grey btn-more">More</a></article>
  <article class="feature" style="left:22px;top:234px"><h3>Consectetur Elit</h3><p>Lorem ipsum dolor sit amet, consectetur adipiscing elit. Curabitur lorem justo, euismod quis feugiat eu, malesuada eget erat. Class aptent taciti sociosqu ad litora torquent per conubia nostra, per inceptos himenaeos.</p><a class="btn-grey btn-more">More</a></article>
  <article class="feature" style="left:263px;top:234px"><h3>Adipiscing Lorem</h3><p>Lorem ipsum dolor sit amet, consectetur adipiscing elit. Curabitur lorem justo, euismod quis feugiat eu, malesuada eget erat. Class aptent taciti sociosqu ad litora torquent per conubia nostra, per inceptos himenaeos.</p><a class="btn-grey btn-more">More</a></article>
  <article class="feature" style="left:499px;top:234px"><h3>Lorem Ipsum Elit</h3><p>Lorem ipsum dolor sit amet, consectetur adipiscing elit. Curabitur lorem justo, euismod quis feugiat eu, malesuada eget erat. Class aptent taciti sociosqu ad litora torquent per conubia nostra, per inceptos himenaeos.</p><a class="btn-grey btn-more">More</a></article>
</main>

<footer class="site-footer">
  <div class="footer-nav">Home | Register | Available Jobs &nbsp;| FAQs | Contact</div>
  <div class="footer-brand">Meridian Crude</div>
  <div class="footer-legal">Terms of Use | Privacy Policy</div>
</footer>
</body>
</html>
```